menu for prepared meals company

Currently have a menu set up with company logo, would like something more eye catching and artistic to make it look professional. This is a fitness and health driven company in regards to purchasing prepared meals to use towards fitness goals. Do not necessarily want the menu to be geared towards muscular men and women. Looking to have the menu be simple to understand, exactly what it stands for, and geared towards a large demographic in health and life style eating changes.

Target Market(s)

health/fitness

Industry/Entity Type

It Company

Requirements
Must have
• *please see set up for mock menu and apply changes that were applied in the word document menu information.
• ex:do not offer sweet potato and chicken hash*

```html
<!DOCTYPE html>
<html lang="en">
<head>
<meta charset="UTF-8">
<title>Fresh Portion Kitchen Menu</title>
<link href="https://fonts.googleapis.com/css2?family=Hind:wght@400;600;700&display=swap" rel="stylesheet">
<style>
  :root {
    --paper: #ffffff;
    --ink: #1c1f1a;
    --brand-red: #e8262f;
    --leaf: #4f8a2b;
    --leaf-soft: #a9cf7c;
    --stalk-light: #f0f8e4;
    --stalk-mid: #d6ebb8;
  }
  html, body {
    margin: 0;
    padding: 0;
    overflow: hidden;
    background: var(--paper);
  }
  .menu {
    position: relative;
    width: 1037px;
    height: 1200px;
    overflow: hidden;
    background: var(--paper);
    font-family: "Hind", "Tahoma", sans-serif;
    color: var(--ink);
    font-size: 17.5px;
    line-height: 23px;
    letter-spacing: 0.55px;
  }
  .menu__artwork {
    position: absolute;
    left: 80px;
    top: 200px;
    width: 830px;
    height: 930px;
    background: radial-gradient(ellipse 42% 56% at 55% 52%, var(--stalk-mid) 0%, var(--stalk-light) 55%, rgba(255,255,255,0) 100%);
  }
  .menu__frame {
    position: absolute;
    inset: 22px;
    border: 1.5px solid var(--leaf-soft);
    border-radius: 14px;
    pointer-events: none;
  }
  .rule {
    position: absolute;
    left: 55px;
    width: 927px;
    height: 0;
  }
  .rule--brand { top: 132px; border-top: 2px solid var(--brand-red); }
  .rule--leaf { border-top: 1px dashed var(--leaf-soft); }
  .brand {
    position: absolute;
    left: 60px;
    top: 62px;
    display: flex;
    align-items: center;
    gap: 10px;
  }
  .brand__mark {
    width: 14px;
    height: 14px;
    border-radius: 50%;
    background: var(--brand-red);
  }
  .brand__name {
    font-size: 23px;
    line-height: 26px;
    font-weight: 700;
    color: var(--brand-red);
    width: 170px;
    letter-spacing: 0.3px;
  }
  .tagline {
    position: absolute;
    left: 262px;
    top: 76px;
    margin: 0;
    font-size: 21px;
    line-height: 26px;
    letter-spacing: 0.4px;
  }
  .line {
    position: absolute;
    left: 55px;
    white-space: nowrap;
  }
  .line--wrap {
    white-space: normal;
    width: 930px;
  }
  .heading { font-weight: 700; }
  .heading--section { color: var(--leaf); }
  .price {
    position: absolute;
    white-space: nowrap;
  }
  .accent { color: var(--brand-red); }
</style>
</head>
<body>
<main class="menu">
  <div class="menu__artwork" role="img" aria-label="Soft backdrop of a tied bunch of fresh green asparagus"></div>
  <div class="menu__frame"></div>

  <header>
    <div class="brand">
      <span class="brand__mark"></span>
      <span class="brand__name">Fresh Portion Kitchen</span>
    </div>
    <p class="tagline">Healthy choices for those who want to change their eating life style</p>
  </header>
  <div class="rule rule--brand"></div>

  <section class="specialty">
    <div class="line heading heading--section" style="top:157px">Specialty Meals</div>
    <div class="line" style="top:191px">Pasta with Turkey Meatballs - Whole grain pasta with turkey meatballs and a tomato sauce</div>
    <div class="line" style="top:225px">Stir fry- Chicken - stir fry vegetable mix with jasmine rice</div>
    <div class="line" style="top:260px">Turkey burger - Turkey Patty on a multigrain flat bread with side of sweet potato fries</div>
    <div class="line line--wrap" style="top:294px">Stuffed Pepper - Pepper stuffed with ground turkey, your choice of whole grain or jasmine rice combined in a red sauce</div>
    <div class="line heading" style="top:350px">All specialty Meals are <span class="accent">$9.95</span></div>
  </section>

  <section class="create-own">
    <div class="line heading heading--section" style="top:384px;left:240px">Create your own</div>
    <div class="line heading" style="top:419px;left:178px">Half size&nbsp; 4oz</div>
    <div class="line heading" style="top:419px;left:366px">Full size&nbsp; 8oz</div>

    <div class="line" style="top:453px">Chicken</div><div class="price" style="top:453px;left:512px">7.95/8.95</div>
    <div class="line" style="top:487px">Ground Beef</div><div class="price" style="top:487px;left:512px">7.95/8.95</div>
    <div class="line" style="top:521px">Ground Turkey</div><div class="price" style="top:521px;left:508px">7.95/8.95</div>
    <div class="line" style="top:555px">Steak</div><div class="price" style="top:555px;left:508px">9.95/10.95</div>
    <div class="line" style="top:590px">Turkey Tenderloin</div><div class="price" style="top:590px;left:508px">7.95/8.95</div>

    <div class="line heading heading--section" style="top:624px;left:240px">All fish portions are 6oz.</div>
    <div class="line" style="top:658px">Salmon</div><div class="price" style="top:658px;left:508px">11.95</div>
    <div class="line" style="top:692px">Tilapia</div><div class="price" style="top:692px;left:508px">10.95</div>
    <div class="line" style="top:727px">Cod</div><div class="price" style="top:727px;left:508px">9.95</div>
    <div class="line" style="top:761px">Veggie Burger</div><div class="price" style="top:761px;left:508px">9.95</div>
  </section>

  <div class="rule rule--leaf" style="top:806px"></div>

  <section class="sides">
    <div class="line heading heading--section" style="top:829px">Carb Choices</div>
    <div class="line heading heading--section" style="top:829px;left:515px">Vegetable Choices</div>
    <div class="line heading" style="top:863px;left:233px">Half Size=1/2 cup Full Size =1cup</div>

    <div class="line" style="top:897px">Whole Grain Pasta</div><div class="price" style="top:897px;left:510px">Green Beans</div>
    <div class="line" style="top:931px">Whole Grain Rice</div><div class="price" style="top:931px;left:513px">Broccoli</div>
    <div class="line" style="top:966px">Jasmine Rice</div><div class="price" style="top:966px;left:513px">Spinach</div>
    <div class="line" style="top:1000px">Gluten free pasta</div><div class="price" style="top:1000px;left:513px">Asparagus</div>

    <div class="line" style="top:1034px">If two vegetable options are wanted choose two for low carb meal combo.</div>
    <div class="line" style="top:1069px">We have delivery within 20 miles for a small fee</div>
  </section>
</main>
</body>
</html>
```